Stationery Design

General Brief:
Corvane Dwellings is a newly established international manufacturing company. We have a manufacturing facility in China and are in the process of building a new facility in Brazil and are expanding into Africa, the Middle East and Western markets by marketing our products through a licensee program. We use production line manufacture processes (similar to the automotive industry) to produce houses, apartments, hotels and accommodation for the resource sector. We will need to be able to differentiate between the various regions that we serve and the market we operate in.

Key Words to describe our business:
International, Global, Professional, Quality, Standard Compliant, Designful, Cost Effective, Experienced

General Brief:
We are looking for good clean design for our letterhead, email signature, Powerpoint presentations, Excel spreadsheets etc. We are looking for templates that can be adopted across the organisation throughout the Microsoft Office suite. Corporate signature files as at November 15 2013 are attached.

Logo Symbolism:
A dot might seem to be an unassuming little thing, the first mark on the pristine sheet of paper. In this case, the dot is a beginning. But see what just happened there? The dot, an essential component in the structure of the sentence, closed it, making it a symbol of ending. Therefore, the dot is both an origination and a conclusion, encompassing all the possibilities of the universe within it, a seed full of potential and a symbol of the supreme being. The dot is also called the "bindhu," which means "drop." The bindhu is a symbol of the absolute, marked on the forehead at the position of the third eye in the place believed to be the seat of the soul. The presence of dots outside or within a symbol can signify the presence of something else. It also acts as reminder of the concept of space and all in all performs as a very positive symbol in the Corvane Dwellings logo.

Target Market(s)

Governments, NGOs, Developers, Investors

Industry/Entity Type

Accommodation

Font styles to use
Other font styles liked:
• in line with corporate signature (logotype)

Requirements
Must have
• Must adhere to corporate signature style and colour codes such as provided in attached documentation. Please be so kind as to design onscreen previews in RGB colours as per attachment.

```html
<!DOCTYPE html>
<html lang="en">
<head>
<meta charset="utf-8">
<title>Corvane Dwellings Letterhead</title>
<link rel="stylesheet" href="https://fonts.googleapis.com/css2?family=Jost:wght@500&display=swap">
<style>
  :root {
    --ink: #0d2b3e;
    --accent: #1aa7e6;
    --paper: #ffffff;
  }
  html, body {
    margin: 0;
    padding: 0;
    overflow: hidden;
    background: var(--paper);
  }
  .letterhead {
    position: relative;
    width: 848px;
    height: 1200px;
    background: var(--paper);
    font-family: "Jost", "Futura", sans-serif;
    color: var(--ink);
    overflow: hidden;
  }
  .brand-name {
    position: absolute;
    top: 64px;
    right: 47px;
    margin: 0;
    font-size: 40px;
    font-weight: 500;
    line-height: 1;
    color: var(--ink);
  }
  .footer-rule {
    position: absolute;
    left: 0;
    top: 1097px;
    width: 848px;
    height: 18px;
  }
  .footer-contact {
    position: absolute;
    left: 0;
    top: 1131px;
    width: 848px;
    text-align: center;
    font-size: 17.5px;
    font-weight: 500;
    line-height: 22px;
  }
  .footer-contact .item {
    margin: 0 12px;
  }
</style>
</head>
<body>
  <main class="letterhead">
    <header>
      <p class="brand-name">Corvane Dwellings</p>
    </header>

    <svg class="footer-rule" viewBox="0 0 848 18" aria-hidden="true">
      <line x1="29" y1="9" x2="848" y2="9" stroke="var(--accent)" stroke-width="2"/>
      <circle cx="29" cy="9" r="8.5" fill="var(--accent)"/>
    </svg>

    <footer class="footer-contact">
      <div>
        <span class="item">www.example.com</span>
        <span class="item">Tel: 00 000 0000</span>
        <span class="item">Fax: 00 000 0000</span>
        <span class="item">Email: info@example.com</span>
      </div>
      <div>Corvane Address Here, 123 Example Street, Example Suburb, Example City</div>
    </footer>
  </main>
</body>
</html>
```